Etiqueta para productos de Panaderia Albores

Necesitamos hacer una actualizacion de nuestra etiqueta con el slogan "Sabor de Siempre", les adjunto foto de la etiqueta actual y fotos de los productos en los cuales utilizamos esta etiqueta.
Somos una empresa de panaderia, ubicados en Honduras
Comercial Trigal SA de CV

Target Market(s)

Clientes en Supermercados

Industry/Entity Type

Panaderia

```html
<!DOCTYPE html>
<html lang="es">
<head>
<meta charset="utf-8">
<title>Panaderia Albores · Sabor de Siempre</title>
<link rel="stylesheet" href="https://fonts.googleapis.com/css2?family=Bebas+Neue&family=Jost:wght@700&family=Montserrat:wght@400;700&family=Nunito+Sans:wght@400;800&display=swap">
<style>
  :root {
    --pink: #e6999c;
    --cream: #ebe3d7;
    --teal: #9fc6c2;
    --teal-soft: #d4e5e2;
    --badge-teal: #a2c9c5;
    --ink: #161b22;
    --charcoal: #444546;
    --wheat-tone: #d8cdbd;
    --portrait-tone: #cfd9d3;
  }
  * { margin: 0; padding: 0; box-sizing: border-box; }
  html, body { width: 900px; height: 1200px; overflow: hidden; background: #ffffff; }
  .label {
    position: relative; width: 900px; height: 1200px;
    border-radius: 70px; overflow: hidden; background: var(--cream);
  }
  .band-top { position: absolute; left: 0; top: 0; width: 900px; height: 445px; background: var(--pink); }
  .band-bottom { position: absolute; left: 0; top: 982px; width: 900px; height: 218px; background: var(--teal); }
  .portrait {
    position: absolute; left: 64px; top: 157px; width: 510px; height: 510px;
    border-radius: 50%; border: 8px solid var(--ink);
    background: radial-gradient(circle at 50% 40%, #f0e6dc 0%, var(--portrait-tone) 55%, #7fbcbc 100%);
  }
  .brand {
    position: absolute; left: 513px; top: 120px; width: 360px;
    display: flex; align-items: center; justify-content: center; gap: 12px;
    font-family: "Jost", sans-serif; font-weight: 700; font-size: 52px;
    letter-spacing: 2px; color: var(--ink);
  }
  .brand-dot { width: 18px; height: 18px; border-radius: 50%; background: var(--ink); }
  .weight-badge { position: absolute; left: 630px; top: 295px; width: 244px; height: 244px; }
  .headline { position: absolute; left: 0; top: 0; width: 900px; height: 1200px; pointer-events: none; }
  .wheat {
    position: absolute; left: 727px; top: 542px; width: 140px; height: 408px;
    border-radius: 70px 70px 20px 20px; background: var(--wheat-tone);
  }
  .feature-icon { position: absolute; }
  .divider { position: absolute; top: 1036px; width: 4px; height: 68px; background: var(--ink); }
  .feature-label {
    position: absolute; top: 1122px; width: 140px; text-align: center;
    font-family: "Montserrat", sans-serif; font-weight: 700; font-size: 12.5px;
    line-height: 16px; color: var(--charcoal);
  }
  .ingredients {
    position: absolute; left: 564px; top: 1018px; width: 304px; height: 140px;
    background: var(--teal-soft); padding: 10px 14px 0 20px;
    font-family: "Nunito Sans", sans-serif; color: #3a3d40;
  }
  .ingredients h2 { font-weight: 800; font-size: 17px; color: var(--ink); margin-bottom: 4px; }
  .ingredients p { font-size: 14px; line-height: 23px; }
</style>
</head>
<body>
<main class="label">
  <div class="band-top"></div>
  <div class="band-bottom"></div>

  <div class="portrait" role="img" aria-label="Ilustración de una abuela sonriente con collar de perlas"></div>

  <div class="brand"><span class="brand-dot"></span>ALBORES</div>

  <svg class="weight-badge" viewBox="0 0 244 244" aria-label="Peso neto 320 gramos">
    <circle cx="122" cy="122" r="116" fill="var(--badge-teal)" stroke="var(--charcoal)" stroke-width="12"/>
    <circle cx="122" cy="122" r="76" fill="none" stroke="var(--charcoal)" stroke-width="2"/>
    <defs>
      <path id="arc-top" d="M 34 122 A 88 88 0 0 1 210 122"/>
      <path id="arc-bottom" d="M 30 122 A 92 92 0 0 0 214 122"/>
    </defs>
    <text font-family="Montserrat, sans-serif" font-size="19" letter-spacing="1.5" fill="var(--charcoal)">
      <textPath href="#arc-top" startOffset="50%" text-anchor="middle">PESO NETO</textPath>
    </text>
    <text font-family="Montserrat, sans-serif" font-size="19" letter-spacing="1.5" fill="var(--charcoal)" dy="16">
      <textPath href="#arc-bottom" startOffset="50%" text-anchor="middle">GRAMOS</textPath>
    </text>
    <text x="122" y="151" text-anchor="middle" font-family="Bebas Neue, sans-serif" font-size="96" fill="var(--charcoal)">320</text>
  </svg>

  <div class="wheat" role="img" aria-label="Ilustración lineal de una espiga de trigo"></div>

  <svg class="headline" viewBox="0 0 900 1200">
    <text x="515" y="648" font-family="Jost, sans-serif" font-weight="700" font-size="52" fill="var(--ink)" textLength="164" lengthAdjust="spacingAndGlyphs">SABOR</text>
    <text x="515" y="700" font-family="Jost, sans-serif" font-weight="700" font-size="52" fill="var(--ink)">DE</text>
    <text x="65" y="884" font-family="Bebas Neue, sans-serif" font-size="232" fill="var(--ink)" textLength="624" lengthAdjust="spacingAndGlyphs">SIEMPRE</text>
    <line x1="57" y1="937" x2="103" y2="937" stroke="var(--charcoal)" stroke-width="2.5"/>
    <line x1="651" y1="937" x2="700" y2="937" stroke="var(--charcoal)" stroke-width="2.5"/>
    <text x="113" y="946" font-family="Montserrat, sans-serif" font-size="25" fill="var(--charcoal)" textLength="527" lengthAdjust="spacing">LOS MEJORES INGGREDIENTES</text>
  </svg>

  <svg class="feature-icon" style="left:65px;top:1033px" width="74" height="72" viewBox="0 0 74 72" aria-hidden="true">
    <rect x="2" y="8" width="50" height="62" rx="10" fill="var(--charcoal)"/>
    <rect x="6" y="0" width="42" height="10" rx="3" fill="var(--charcoal)"/>
    <circle cx="27" cy="38" r="11" fill="none" stroke="var(--teal)" stroke-width="3"/>
    <path d="M27 30 V48" stroke="var(--teal)" stroke-width="3"/>
    <circle cx="56" cy="54" r="19" fill="var(--teal)"/>
    <path d="M40 52 H72 A16 16 0 0 1 40 52 Z" fill="var(--charcoal)"/>
    <path d="M44 48 A12 9 0 0 1 68 48 Z" fill="var(--charcoal)"/>
  </svg>
  <div class="divider" style="left:188px"></div>
  <svg class="feature-icon" style="left:247px;top:1047px" width="86" height="44" viewBox="0 0 86 44" aria-hidden="true">
    <path d="M4 40 C0 24 14 4 43 4 C72 4 86 24 82 40 Z" fill="var(--charcoal)"/>
    <path d="M24 10 L30 26 M42 7 L44 24 M58 10 L54 26" stroke="var(--teal)" stroke-width="3" stroke-linecap="round"/>
  </svg>
  <div class="divider" style="left:382px"></div>
  <svg class="feature-icon" style="left:437px;top:1030px" width="72" height="72" viewBox="-36 -36 72 72" aria-hidden="true">
    <g stroke="var(--charcoal)" stroke-width="4" stroke-linecap="round" fill="none">
      <g id="flake-arm"><path d="M0 -34 V34 M-8 -26 L0 -18 L8 -26 M-8 26 L0 18 L8 26"/></g>
      <use href="#flake-arm" transform="rotate(60)"/>
      <use href="#flake-arm" transform="rotate(120)"/>
    </g>
  </svg>

  <div class="feature-label" style="left:31px">LOS MEJORES<br>INGREDIENTES</div>
  <div class="feature-label" style="left:220px">PAN<br>ARTESENAL</div>
  <div class="feature-label" style="left:403px">RECOMENDAMOS<br>REFRIGERAR</div>

  <section class="ingredients">
    <h2>Ingredientes:</h2>
    <p>Agua, sal, margarina, azúcar,<br>esencia de vainilla, preservantes<br>y polvo de hornear. Contiene huevos,<br>leche en polvo y trigo.</p>
  </section>
</main>
</body>
</html>
```